Vero M.Q. - Diagnostic Ultrasound Flyer

About US
Vero M.Q. is a concierge ultrasound company that provides onsite or offsite diagnostic ultrasounds. We have over 14 years experience in sonography, business management, and customer service. We offer both the physician and patient flexibility, convenience, and access to timely services.

We provide ultrasounds for the following specialties:
Obstetrics/Gynecology
Abdominal
Small Parts
Vascular

Company Features:
1. Onsite or Offsite Scans
2. Images Available Immediately for Referring Physician and Patient
3. Flexible Options for Ultrasound Interpretation/Billing
4. Access to Interpreting Radiologist
5. Final Report Process - 1-2 Business Days/ 1 hour for STAT.
6. PACS Storage with Secure Access.

We need a place to add in our contact information (address, email, website, phone)

We already have a logo and would like to use it ( they are attached). We would the colors to match the logo colors....maybe lighter version of yellow and blue.

```html
<!DOCTYPE html>
<html lang="en">
<head>
<meta charset="utf-8">
<title>Vero M.Q. – Diagnostic Ultrasound Flyer</title>
<link rel="stylesheet" href="https://fonts.googleapis.com/css2?family=Poppins:wght@400;500;600;700;800&display=swap">
<style>
  :root {
    --brand-blue: #2e3a93;
    --brand-blue-soft: #4450a6;
    --brand-yellow: #fbbf2f;
    --ink: #161616;
    --paper: #ffffff;
    --photo-gray-1: #d9d9d9;
    --photo-gray-2: #8d8d8d;
    --photo-blue-1: #cfe3f5;
    --photo-blue-2: #7fb3e3;
  }
  * { box-sizing: border-box; margin: 0; padding: 0; }
  html, body { width: 849px; height: 1200px; overflow: hidden; background: var(--paper); }
  body { font-family: "Poppins", sans-serif; color: var(--ink); }

  .flyer { position: relative; width: 849px; height: 1200px; overflow: hidden; background: var(--paper); }

  .top-accent {
    position: absolute; left: 0; top: 0; width: 447px; height: 35px;
    background: var(--brand-yellow); border-bottom-right-radius: 30px;
  }

  .hero-photo {
    position: absolute; left: 390px; top: 0; width: 459px; height: 340px;
    background: linear-gradient(135deg, var(--photo-gray-1), var(--photo-gray-2));
    clip-path: polygon(95px 0, 100% 0, 100% 100%, 0 100%, 0 165px, 95px 165px);
  }

  .brand { position: absolute; left: 28px; top: 58px; z-index: 2; }
  .brand-name {
    font-size: 60px; font-weight: 800; line-height: 1; letter-spacing: 3px;
    color: var(--brand-blue);
  }
  .brand-tagline { margin-top: 8px; font-size: 24px; font-weight: 400; line-height: 1; color: var(--ink); white-space: nowrap; }

  .hero-shapes { position: absolute; left: 0; top: 0; width: 849px; height: 470px; }

  .specialty-icon {
    position: absolute; left: 133px; top: 204px; width: 106px; height: 102px;
    border-radius: 14px; background: var(--brand-blue-soft);
  }

  .hero-title {
    position: absolute; left: 38px; top: 310px;
    font-size: 51px; font-weight: 600; line-height: 63px; color: var(--paper);
    letter-spacing: 0.5px;
  }

  .experience {
    position: absolute; left: 500px; top: 338px; width: 360px; text-align: center;
    font-size: 25px; line-height: 33px; font-weight: 600; color: var(--ink);
  }
  .experience-highlight { display: block; color: var(--brand-blue); }
  .experience-highlight strong { font-weight: 800; }

  .features { position: absolute; left: 37px; top: 489px; list-style: none; }
  .feature {
    position: relative; padding-left: 28px;
    font-size: 27px; line-height: 39px; font-weight: 400; color: var(--ink);
    white-space: nowrap;
  }
  .feature-tick { position: absolute; left: 0; top: 11px; width: 20px; height: 20px; }

  .specialty-band {
    position: absolute; left: 0; top: 790px; width: 660px; height: 215px;
    background: var(--brand-blue);
  }
  .band-decor {
    position: absolute; left: 408px; top: 20px; width: 190px; height: 175px;
    border-radius: 20px; background: var(--brand-blue-soft); opacity: 0.7;
  }
  .specialty-list { position: absolute; left: 50px; top: 4px; line-height: 65px; font-size: 55px; }
  .specialty-list .soft { color: var(--brand-yellow); font-weight: 400; display: block; letter-spacing: 1px; }
  .specialty-list .strong { color: var(--paper); font-weight: 700; display: block; letter-spacing: 1px; }

  .staff-photo {
    position: absolute; left: 545px; top: 735px; width: 304px; height: 465px;
    border-top-left-radius: 150px; border-top-right-radius: 150px;
    background: linear-gradient(180deg, var(--photo-blue-1), var(--photo-blue-2));
  }

  .contact { position: absolute; left: 30px; top: 1051px; list-style: none; }
  .contact-item {
    display: flex; align-items: center; gap: 10px;
    font-size: 27px; line-height: 38.5px; font-weight: 400; color: var(--ink);
  }
  .contact-icon { width: 24px; height: 24px; flex: none; }
</style>
</head>
<body>
<main class="flyer">
  <div class="top-accent"></div>

  <div class="hero-photo" role="img" aria-label="Photo of a sonographer performing a neck ultrasound on a reclining patient beside a monitor"></div>

  <header class="brand">
    <div class="brand-name">Vero M.Q.</div>
    <div class="brand-tagline">concierge ultrasound company</div>
  </header>

  <svg class="hero-shapes" viewBox="0 0 849 470" aria-hidden="true">
    <path d="M0,173 H300 Q332,173 356,198 L478,366 L370,470 H0 Z" fill="var(--brand-blue)"/>
    <path d="M440,372 Q520,318 610,320 H849 V424 H575 Q520,420 480,376 Z" fill="var(--paper)"/>
    <path d="M384,470 L481,376 Q522,424 578,424 H849 V470 Z" fill="var(--brand-blue)"/>
  </svg>

  <div class="specialty-icon" role="img" aria-label="Pictogram of a doctor with a stethoscope examining a pregnant woman"></div>

  <h1 class="hero-title">OBSTETRICS<br>GYNECOLOGY</h1>

  <p class="experience">WE HAVE OVER<span class="experience-highlight"><strong>14 YEARS</strong> EXPERIENCE</span></p>

  <ul class="features">
    <li class="feature"><svg class="feature-tick" viewBox="0 0 20 20" aria-hidden="true"><circle cx="10" cy="10" r="8" fill="none" stroke="var(--brand-blue)" stroke-width="1.8"/><path d="M5.5 10 L9 13.5 L17 4" fill="none" stroke="var(--brand-blue)" stroke-width="2.4" stroke-linecap="round" stroke-linejoin="round"/></svg>Onsite or Offsite Scans</li>
    <li class="feature"><svg class="feature-tick" viewBox="0 0 20 20" aria-hidden="true"><circle cx="10" cy="10" r="8" fill="none" stroke="var(--brand-blue)" stroke-width="1.8"/><path d="M5.5 10 L9 13.5 L17 4" fill="none" stroke="var(--brand-blue)" stroke-width="2.4" stroke-linecap="round" stroke-linejoin="round"/></svg>Images Available Immediately<br>for Referring Physician and Patient</li>
    <li class="feature"><svg class="feature-tick" viewBox="0 0 20 20" aria-hidden="true"><circle cx="10" cy="10" r="8" fill="none" stroke="var(--brand-blue)" stroke-width="1.8"/><path d="M5.5 10 L9 13.5 L17 4" fill="none" stroke="var(--brand-blue)" stroke-width="2.4" stroke-linecap="round" stroke-linejoin="round"/></svg>Flexible Options for Ultrasound Interpretation/Billing</li>
    <li class="feature"><svg class="feature-tick" viewBox="0 0 20 20" aria-hidden="true"><circle cx="10" cy="10" r="8" fill="none" stroke="var(--brand-blue)" stroke-width="1.8"/><path d="M5.5 10 L9 13.5 L17 4" fill="none" stroke="var(--brand-blue)" stroke-width="2.4" stroke-linecap="round" stroke-linejoin="round"/></svg>Access to Interpreting Radiologist</li>
    <li class="feature"><svg class="feature-tick" viewBox="0 0 20 20" aria-hidden="true"><circle cx="10" cy="10" r="8" fill="none" stroke="var(--brand-blue)" stroke-width="1.8"/><path d="M5.5 10 L9 13.5 L17 4" fill="none" stroke="var(--brand-blue)" stroke-width="2.4" stroke-linecap="round" stroke-linejoin="round"/></svg>Final Report Process - 1-2 Business Days/ 1 hour for STAT.</li>
    <li class="feature"><svg class="feature-tick" viewBox="0 0 20 20" aria-hidden="true"><circle cx="10" cy="10" r="8" fill="none" stroke="var(--brand-blue)" stroke-width="1.8"/><path d="M5.5 10 L9 13.5 L17 4" fill="none" stroke="var(--brand-blue)" stroke-width="2.4" stroke-linecap="round" stroke-linejoin="round"/></svg>PACS Storage with Secure Access.</li>
  </ul>

  <section class="specialty-band">
    <div class="band-decor" role="img" aria-label="Faint pictogram of a doctor examining a pregnant woman"></div>
    <h2 class="specialty-list">
      <span class="soft">ABDOMINAL</span>
      <span class="soft">SMALL PARTS</span>
      <span class="strong">VASCULAR</span>
    </h2>
  </section>

  <div class="staff-photo" role="img" aria-label="Photo of a smiling nurse in blue scrubs with a stethoscope holding a clipboard"></div>

  <ul class="contact">
    <li class="contact-item"><svg class="contact-icon" viewBox="0 0 24 24" aria-hidden="true"><circle cx="12" cy="12" r="10.5" fill="none" stroke="var(--brand-blue)" stroke-width="1.6"/><rect x="6.5" y="8" width="11" height="8" rx="1" fill="var(--brand-blue)"/><path d="M6.8 8.5 L12 12.5 L17.2 8.5" fill="none" stroke="var(--paper)" stroke-width="1.2"/></svg>hello@veromq-scan.com</li>
    <li class="contact-item"><svg class="contact-icon" viewBox="0 0 24 24" aria-hidden="true"><circle cx="12" cy="12" r="10.5" fill="none" stroke="var(--brand-blue)" stroke-width="1.6"/><circle cx="12" cy="12" r="6.5" fill="none" stroke="var(--brand-blue)" stroke-width="1.3"/><ellipse cx="12" cy="12" rx="3" ry="6.5" fill="none" stroke="var(--brand-blue)" stroke-width="1.2"/><path d="M5.5 12 H18.5 M6.5 9 H17.5 M6.5 15 H17.5" stroke="var(--brand-blue)" stroke-width="1.1"/></svg>www.veromq-scan.com</li>
    <li class="contact-item"><svg class="contact-icon" viewBox="0 0 24 24" aria-hidden="true"><circle cx="12" cy="12" r="10.5" fill="none" stroke="var(--brand-blue)" stroke-width="1.6"/><path d="M12 18 C9 14.5 8 12.5 8 10.5 A4 4 0 0 1 16 10.5 C16 12.5 15 14.5 12 18 Z" fill="none" stroke="var(--brand-blue)" stroke-width="1.4"/><circle cx="12" cy="10.5" r="1.5" fill="var(--brand-blue)"/></svg>42 Elm Ave, Riverbend City</li>
  </ul>
</main>
</body>
</html>
```